Design Large Inspirational Artwork with Long Quote

Design a large piece of art with a quote from Marcus Hallwell.

QUOTE
"The thing that's so interesting about being alive is that you're all in. No matter what you do, you're all in. This is gonna kill you, so I think you might as well play the most magnificent game you can while you're waiting. Because, do you have anything better to do? Why not pick the best thing possible that you could do? Because you're more powerful than you think, way more powerful than you think. I mean, God only knows what you are in the final analysis. You're blind to your own weaknesses, but you're also blind to your own strengths. How far could you take that if you stopped wasting time, and if you stopped lying, and if you oriented yourself to the highest possible good that you could conceive of and you committed to that? How much good could you do? Well, I would say: why don't you find out?"

SIZE
A high-resolution print size of 6' wide and 3' tall should provide ample space for both the quote and the accompanying artwork.

TYPOGRAPHY
Choose a bold, clean, and easily readable font for the quote. You could also experiment with different font sizes for certain words or phrases to emphasize their importance within the quote.

COLORS
Since the quote is thought-provoking and reflective, you might want to use a color palette that evokes a sense of introspection and depth. Consider using cool, calming colors like shades of blue, gray, or green. Alternatively, you can use a contrasting color scheme with a light background and dark text to make the quote stand out.

ARTWORK
Select / create / edit background artwork to complement the quote.
While a great design might be minimalistic and/or greyscale, I'd really like to see some full color options. This might be anything from photography or graphics inspired by the ideas in the text, to abstract colors or illustrations that feel like the sentiment expressed.
The art should capture your attention and encourage you to read the text. The art should be visually appealing, both at a distance and up close, regardless of whether the text is read.
Updates

Having trouble confirming the exact print size.

Still looking for printing solution and final size confirmation.

Target Market(s)

Personal, business, office

Industry/Entity Type

None

Font styles to use
Sans Serif
Script

Requirements
Must have
• Entire quote, legible text, modern design, attractive artwork, approx 6ft wide and 3ft tall
Nice to have
• Different font (sizes) for certain words or phrases to emphasize their importance within the quote.

```html
<!DOCTYPE html>
<html lang="en">
<head>
<meta charset="utf-8">
<title>Why Don't You Find Out — Quote Artwork</title>
<link rel="stylesheet" href="https://fonts.googleapis.com/css2?family=Caveat:wght@400;700&family=Caveat+Brush&display=swap">
<style>
  :root {
    --page-bg: #e6e6e6;
    --art-deep: #12061c;
    --art-mid: #2c0f40;
    --art-glow: #5a2585;
    --art-violet: #6a3fb0;
    --text-light: #ffffff;
  }
  * { margin: 0; padding: 0; box-sizing: border-box; }
  html, body {
    width: 1200px;
    height: 1200px;
    overflow: hidden;
    background: var(--page-bg);
  }
  .canvas {
    position: relative;
    width: 1200px;
    height: 1200px;
  }
  .artwork {
    position: absolute;
    left: 40px;
    top: 320px;
    width: 1120px;
    height: 560px;
    overflow: hidden;
  }
  .artwork__background {
    position: absolute;
    inset: 0;
    background:
      radial-gradient(ellipse 40% 30% at 78% 66%, rgba(106, 63, 176, 0.55), transparent 70%),
      radial-gradient(ellipse 55% 50% at 50% 30%, rgba(90, 37, 133, 0.7), transparent 75%),
      radial-gradient(ellipse 90% 80% at 50% 50%, var(--art-mid), var(--art-deep) 100%);
  }
  .quote {
    position: absolute;
    inset: 0;
    display: flex;
    flex-direction: column;
    justify-content: center;
    align-items: center;
    text-align: center;
    color: var(--text-light);
    font-family: "Caveat", cursive;
    font-size: 21px;
    line-height: 41px;
    letter-spacing: 0.2px;
  }
  .quote__line { display: block; white-space: nowrap; }
  .quote__emphasis {
    font-family: "Caveat Brush", "Caveat", cursive;
    font-size: 27px;
    letter-spacing: 0.4px;
  }
</style>
</head>
<body>
<div class="canvas">
  <section class="artwork">
    <div class="artwork__background" role="img" aria-label="Abstract textured background in deep purple and violet paint splashes"></div>
    <blockquote class="quote">
      <span class="quote__line">The thing that’s so interesting about <span class="quote__emphasis">being alive</span> is that you’re all in.</span>
      <span class="quote__line">No matter what you do, you’re all in. This is gonna <span class="quote__emphasis">kill you</span>, so I think</span>
      <span class="quote__line">you might as well <span class="quote__emphasis">play</span> the most magnificent game you can while you’re waiting.</span>
      <span class="quote__line">Because, do you have anything <span class="quote__emphasis">better to do?</span></span>
      <span class="quote__line">Why not pick the <span class="quote__emphasis">best thing</span> possible that you could do?</span>
      <span class="quote__line">Because you’re more <span class="quote__emphasis">powerful</span> than you think, way more powerful</span>
      <span class="quote__line">than you think. I mean, God only knows what you are in the <span class="quote__emphasis">final analysis.</span></span>
      <span class="quote__line">You’re <span class="quote__emphasis">blind</span> to your own weaknesses, but you’re also blind to your own strengths.</span>
      <span class="quote__line">How far could you take that if you stopped <span class="quote__emphasis">wasting time</span>, and if you stopped lying,</span>
      <span class="quote__line">and if you oriented yourself to <span class="quote__emphasis">the highest</span> possible good that you could conceive</span>
      <span class="quote__line">of and you <span class="quote__emphasis">committed</span> to that? How much good could you do?</span>
      <span class="quote__line">Well, I would say: <span class="quote__emphasis">why don’t you find out?</span></span>
    </blockquote>
  </section>
</div>
</body>
</html>
```